Business Card Design Project

Business card incoporating newly designed logo. The business cards will be magnets and I would like the same design as previously provided (Blue colour swatch with logo up the top) Please note that the logo incorporates a website so it needs to be legible.
The blue colours in teh swatch ideally will be in the same range as the blue of the logo.
The copy should all be in the same colour ie. black if in the white lines or white if in the swatch itself
Updates

Hi All

Some of the designs are very close to what I am after.  I have added logo and updated brief to assist with design.  This project is not refundable so I will be selecting a design.

Hi All

We are looking for a business card as per the brief (colour swatch style) as mentioned it is also a magnet so it needs to be created to the specs supplied.  Being a magnet there is also no requirment for reverse design.

Cheers
Marcy

Industry/Entity Type

Business

Requirements
Must have
• Blue colour swatch design. (see attached current example)
KW Coatings logo (colour) up the top
I require 1 design but 2 versions (with two peoples names and mobile numbers)

The magnets will be printed by PrintHollow.com.au And you can find the full specs online http://www.printhollow.com.au/custom-magnets.aspx

```html
<!DOCTYPE html>
<html lang="en">
<head>
<meta charset="utf-8">
<title>KW Coatings – Magnet Cards</title>
<link rel="stylesheet" href="https://fonts.googleapis.com/css2?family=Questrial&display=swap">
<style>
  :root {
    --page: #ffffff;
    --ink: #111111;
    --frame: #1a1a1a;
    --logo-bg: #e8e2b0;
    --brand-blue: #1e7fc8;
    --swatch-1: #0010b0;
    --swatch-2: #1440ff;
    --swatch-3: #1c44d4;
    --swatch-4: #96b7ea;
  }
  * { box-sizing: border-box; margin: 0; padding: 0; }
  html, body {
    width: 1200px; height: 972px; overflow: hidden;
    background: var(--page);
    font-family: "Questrial", "Century Gothic", sans-serif;
    color: var(--ink);
  }
  .sheet { position: relative; width: 1200px; height: 972px; }
  .card {
    position: absolute; top: 0; width: 563px; height: 972px;
    border: 2px solid var(--frame);
    display: grid;
    grid-template-rows: 160px 147px 50px 146px 62px 146px 55px 146px 1fr;
  }
  .card--first { left: 0; }
  .card--second { left: 637px; }
  .brand {
    background: var(--logo-bg);
    padding: 22px 0 0 16px;
  }
  .brand__name {
    font-size: 64px; line-height: 1; color: var(--brand-blue);
    letter-spacing: -1px; white-space: nowrap;
  }
  .brand__web {
    margin-top: 8px; font-size: 14px; color: var(--brand-blue);
  }
  .swatch--1 { background: var(--swatch-1); }
  .swatch--2 { background: var(--swatch-2); }
  .swatch--3 { background: var(--swatch-3); }
  .swatch--4 { background: var(--swatch-4); }
  .line {
    background: var(--page);
    display: flex; align-items: center;
    padding-left: 14px;
    font-size: 31px; white-space: nowrap;
  }
  .line--name { padding-top: 6px; }
</style>
</head>
<body>
<main class="sheet">
  <section class="card card--first" aria-label="Business card – Kevin Walsh">
    <header class="brand">
      <div class="brand__name">KW Coatings</div>
      <div class="brand__web">kwcoatings.com.au</div>
    </header>
    <div class="swatch swatch--1"></div>
    <p class="line line--name">Kevin Walsh</p>
    <div class="swatch swatch--2"></div>
    <p class="line line--phone">0400 555 017</p>
    <div class="swatch swatch--3"></div>
    <p class="line line--service">Commercial &amp; Domestic Painting</p>
    <div class="swatch swatch--4"></div>
    <p class="line line--email">kevinwalshcoatings@mailbox.com</p>
  </section>

  <section class="card card--second" aria-label="Business card – Dean Foley">
    <header class="brand">
      <div class="brand__name">KW Coatings</div>
      <div class="brand__web">kwcoatings.com.au</div>
    </header>
    <div class="swatch swatch--1"></div>
    <p class="line line--name">Dean Foley</p>
    <div class="swatch swatch--2"></div>
    <p class="line line--phone">0400 5550 0328</p>
    <div class="swatch swatch--3"></div>
    <p class="line line--service">Commercial &amp; Domestic Painting</p>
    <div class="swatch swatch--4"></div>
    <p class="line line--email">kevinwalshcoatings@mailbox.com</p>
  </section>
</main>
</body>
</html>
```